Events and Parties web-site needs a Web Design

ZorVeno needs a web design.
ZorVeno means The Bees in Italian.
ZorVeno target market is people who is organizing parties and events.
Our mission is that the parties and events of our clients exceed their expectations by providing them web and mobile tools.
Our vision is to be the best and biggest party web portal of the country.
The main features of our web site is to let people invite guests and search suppliers/providers. Guests will also confirm presence (RSVP) and buy presents/gifts at the site as well.
Our slogan is "Curta sua festa desde já !" that means "Enjoy our party now !" in Brazilian Portuguese.
The idea here is that the party starts now and not only at the scheduled date and time.
Updates
It seems that must have and nice to have briefing is not appearing to you as I filled. So I will type it agai here:
Our slogan text that is "Curta sua festa desde já !" that means "Enjoy your party now !".
Space to paid ads.
Language switch to Spanish. Brazilian Portuguese is our default language.
Logon form with 2 inputs: Email and password.
RSVP form with 2 inputs: Event ID and password
Plivex trusted site seal (SSL/HTTPS) logo.
Update to my briefing: Only event organizer and guests will be able to see details of the events/parties like photos/blog, guest list and etc. Suppliers will be searched and rated like stayvorta.com/wandrikel.
Target Market(s)
ZorVeno target market is amateur and professional people who are organizing parties and events.
Our mission is that the parties and events of our clients exceed their expectations by providing them easy and fast web and mobile tools.
Our vision is to be the best and biggest party portal of our country.
The main features of our web site is to let people invite guests and search suppliers/providers. Guests will also confirm presence (RSVP) and buy presents at the site.
Industry/Entity Type
Events
Requirements
Must have
- Design and colors compliant with attached logo.
- Our slogan text that is "Curta sua festa desde já !" that means "Enjoy your party now !".
- Space to paid ads.
- Language switch to Spanish. Brazilian Portuguese is our default language.
- Logon form with 2 inputs: Email and password.
- RSVP form with 2 inputs: Event ID and password
- Plivex trusted site seal (SSL/HTTPS) logo.
Nice to have
- ZorVeno stands for The Bees in Italian. It would be very nice to have a not so explicit idea that each user is a bee and ZorVeno is the hive where party/event occurs.
Should not have
- No PageMolder please.
- No infant/child oriented designs please. Our market is not only children birthdays but also other parties and events like marriages, corporate events and so on

```html
<!DOCTYPE html>
<html lang="en">
<head>
<meta charset="utf-8">
<title>ZorVeno – Events and Parties</title>
<link rel="stylesheet" href="https://fonts.googleapis.com/css2?family=Raleway:wght@400;500;600;700&family=Open+Sans:wght@400;600;700&display=swap">
<style>
:root{
  --orange:#f5b31b;
  --orange-deep:#ef9f10;
  --brown:#3b1d12;
  --brown-soft:#5a3324;
  --ink:#333333;
  --muted:#8a8a8a;
  --line:#e4e4e4;
  --band:#e6e6e6;
  --cream:#fbf3e3;
  --white:#ffffff;
  --dark:#2d2d2d;
}
*{box-sizing:border-box;margin:0;padding:0}
html,body{width:1200px;height:3460px;overflow:hidden}
body{font-family:"Open Sans",Arial,sans-serif;color:var(--ink);background:var(--white);font-size:13px;line-height:1.55}
h1,h2,h3,h4{font-family:"Raleway",Arial,sans-serif;font-weight:500}
.wrap{width:1040px;margin:0 auto;position:relative}

/* header */
.top-line{height:6px;background:var(--brown)}
.site-header{height:106px;border-bottom:1px solid var(--line)}
.site-header .wrap{display:flex;align-items:center;height:106px}
.brand{display:flex;align-items:center;gap:10px}
.brand-dot{width:30px;height:30px;border-radius:50%;background:var(--orange)}
.brand-name{font-family:"Raleway",sans-serif;font-size:30px;font-weight:700;color:var(--brown)}
.brand-tag{font-size:11px;color:var(--muted);width:150px;margin-left:14px;line-height:1.35}
.main-nav{display:flex;margin-left:auto;margin-right:24px}
.main-nav a{font-family:"Raleway",sans-serif;font-size:12px;font-weight:700;color:var(--dark);text-decoration:none;padding:14px 14px;text-transform:uppercase}
.main-nav a.active{background:var(--brown);color:var(--white)}
.header-box{background:var(--orange);color:var(--white);padding:14px 16px;font-weight:700;font-size:13px;line-height:1.6;text-align:center}
.header-box small{display:block;font-size:11px;font-weight:600}

/* hero */
.hero{height:480px;position:relative;background:linear-gradient(120deg,#e8c9c0 0%,#c94b4b 35%,#f1e4dc 62%,#e7d2b5 100%)}
.hero-slogan{position:absolute;left:160px;top:140px;background:rgba(0,0,0,.55);color:var(--white);font-family:"Raleway",sans-serif;font-size:28px;font-weight:500;padding:10px 22px}
.hero-arrow{position:absolute;top:215px;width:36px;height:36px;border-radius:50%;background:rgba(255,255,255,.8)}
.hero-arrow.prev{left:14px}.hero-arrow.next{right:14px}
.hero-arrow svg{display:block;margin:11px auto}
.hero-panel{position:absolute;right:40px;top:0;width:340px;height:464px;background:var(--brown);padding:22px 24px;color:var(--white)}
.panel-title{font-family:"Raleway",sans-serif;font-weight:700;font-size:15px;margin-bottom:10px}
.field{height:34px;background:var(--white);margin-bottom:10px;color:#999;font-size:12px;padding:8px 10px}
.field-row{display:flex;gap:10px;align-items:center;font-size:12px;margin-bottom:12px}
.field-row .field{margin:0;flex:1;height:30px;padding:6px 10px}
.btn-orange{display:block;background:var(--orange);color:var(--white);text-align:center;font-weight:700;font-size:12px;padding:8px;margin:0 auto 22px;width:140px}
.btn-orange.wide{width:100%}
.panel-split{height:1px;background:var(--brown-soft);margin-bottom:16px}
.range{height:4px;background:var(--white);margin:14px 0 22px;position:relative}
.range span{position:absolute;left:30%;width:40%;top:0;bottom:0;background:var(--orange)}

/* section title */
.section-title{font-family:"Raleway",sans-serif;font-size:26px;color:var(--dark);font-weight:500}
.section-title.center{text-align:center}

/* categories */
.categories{padding:38px 0 30px}
.cat-grid{display:flex;gap:40px;margin-top:26px}
.cat-item{flex:1}
.cat-head{display:flex;align-items:center;gap:12px;margin-bottom:14px}
.cat-icon{width:46px;height:46px;border-radius:50%;border:2px solid var(--orange);display:flex;align-items:center;justify-content:center;flex:none}
.cat-head h3{font-size:15px;color:var(--orange-deep);font-weight:600;line-height:1.2}
.cat-item p{font-size:12px;color:var(--muted)}

/* ads */
.ad-band{height:110px;background:var(--band);position:relative;overflow:hidden}
.ad-band .wrap{height:110px;display:flex;align-items:center}
.ad-label{font-family:"Raleway",sans-serif;font-size:46px;color:#555;letter-spacing:2px;font-weight:400}
.ad-offer{position:absolute;right:0;top:22px;height:66px;background:var(--dark);color:var(--white);font-family:"Raleway",sans-serif;font-size:20px;display:flex;align-items:center;padding:0 40px 0 60px;clip-path:polygon(40px 0,100% 0,100% 100%,0 100%)}
.ad-offer.tall{top:0;height:110px;font-size:26px;line-height:1.2;text-align:center;padding:0 50px 0 90px;clip-path:polygon(70px 0,100% 0,100% 100%,0 100%)}

/* gifts */
.gifts{padding:34px 0 40px;height:416px}
.gift-body{display:flex;gap:40px;margin-top:22px}
.gift-photo{width:400px;height:240px;background:linear-gradient(135deg,#b9c28a,#e7d9a8 50%,#c23b2c);position:relative}
.price{position:absolute;right:-30px;top:-22px;width:90px;height:90px;border-radius:50%;background:var(--orange);color:var(--white);font-family:"Raleway",sans-serif;font-weight:700;font-size:22px;display:flex;align-items:center;justify-content:center;border:5px solid var(--white)}
.gift-text{flex:1;padding-left:30px;padding-top:6px}
.gift-text h3{font-size:36px;color:var(--dark);font-weight:500;margin-bottom:16px}
.gift-text p{font-size:12px;color:var(--muted);margin-bottom:10px}
.pager{display:flex;gap:10px;justify-content:flex-end;margin-top:30px}
.pager span{width:32px;height:32px;border-radius:50%;border:2px solid var(--orange);display:flex;align-items:center;justify-content:center}

/* suppliers */
.suppliers{background:var(--cream);height:520px;padding:40px 0}
.sup-grid{display:flex;gap:24px;margin-top:40px}
.sup-card{flex:1;background:var(--white);padding:14px 14px 22px;text-align:center}
.sup-photo{height:128px;margin-bottom:16px}
.stars{color:var(--orange);font-size:15px;letter-spacing:2px}
.stars .off{color:#cfcfcf}
.sup-card h4{font-size:14px;font-weight:600;color:var(--dark);margin:6px 0 10px}
.sup-card p{font-size:11px;color:var(--muted);line-height:1.5}

.spacer{height:60px}

/* events */
.events{padding:32px 0 30px;height:620px}
.event-list{margin-top:26px}
.event{display:flex;background:#f7f3ea;margin-bottom:14px;padding:22px 20px;height:160px}
.event-thumb{width:76px;height:76px;margin-right:20px;flex:none}
.event-main{flex:1;padding-right:30px;border-right:1px solid var(--line)}
.event-main h4{font-size:18px;font-weight:700;color:var(--dark);margin-bottom:6px}
.event-main p{font-size:11px;color:var(--muted);line-height:1.6}
.event-main .link{color:var(--orange-deep)}
.event-meta{width:150px;padding-left:26px;font-size:11px;color:var(--muted);display:flex;flex-direction:column;justify-content:center;gap:6px}
.event-meta b{color:var(--orange-deep);font-weight:600}

/* testimonials */
.testimonials{background:var(--cream);height:360px;padding:44px 0}
.quote-box{margin-top:30px;background:var(--orange);height:140px;position:relative;color:var(--white);text-align:center;padding:30px 120px}
.quote-box p{font-family:"Raleway",sans-serif;font-size:18px;font-weight:600;line-height:1.4}
.quote-box .more{display:inline-block;font-size:11px;margin-top:10px}
.quote-nav{position:absolute;left:0;bottom:0;display:flex}
.quote-nav span{width:28px;height:28px;background:var(--dark);display:flex;align-items:center;justify-content:center;margin-right:2px}
.quote-author{text-align:right;margin-top:14px;font-size:12px;color:var(--dark)}

/* footer */
.site-footer{padding:40px 0 0;height:316px}
.foot-grid{display:flex;gap:60px}
.foot-col{flex:1}
.foot-col h4{font-size:16px;font-weight:700;color:var(--dark);margin-bottom:16px}
.contact-line{display:flex;gap:10px;align-items:center;font-size:11px;color:var(--muted);margin-bottom:8px}
.contact-line i{width:16px;height:16px;border-radius:50%;background:var(--orange);flex:none}
.social{display:flex;gap:8px;margin-top:14px}
.social span{width:28px;height:28px;border-radius:50%;border:2px solid var(--orange)}
.post{display:flex;gap:10px;margin-bottom:12px}
.post-thumb{width:48px;height:40px;flex:none}
.post p{font-size:11px;color:var(--muted);line-height:1.4}
.post a{font-size:11px;color:var(--orange-deep);text-decoration:none}
.faces{display:grid;grid-template-columns:repeat(4,52px);gap:8px}
.faces span{height:52px;display:block}
.foot-bottom{border-top:1px solid var(--line);height:46px}
.foot-bottom .wrap{display:flex;align-items:center;height:46px;font-size:11px;color:var(--muted)}
.foot-links{margin-left:auto;display:flex;gap:6px}
.foot-links a{color:var(--dark);text-decoration:none;padding:4px 10px}
.foot-links a.active{background:var(--orange);color:var(--white)}
</style>
</head>
<body>

<div class="top-line"></div>
<header class="site-header">
  <div class="wrap">
    <div class="brand">
      <span class="brand-dot"></span>
      <span class="brand-name">ZorVeno</span>
    </div>
    <p class="brand-tag">A plataforma digital para você organizar seu evento</p>
    <nav class="main-nav">
      <a class="active" href="#">Home</a>
      <a href="#">Parties &amp; Events</a>
      <a href="#">Invite Guests</a>
      <a href="#">Buy Gifts</a>
      <a href="#">Blog</a>
      <a href="#">Contact</a>
    </nav>
    <div class="header-box">(555) 014 2290<small>LOGIN ▾</small></div>
  </div>
</header>

<section class="hero">
  <div role="img" aria-label="Party dessert table with red cake and sweets" style="position:absolute;inset:0"></div>
  <div class="hero-slogan">Enjoy Your Party Now !</div>
  <span class="hero-arrow prev"><svg width="14" height="14" viewBox="0 0 14 14"><path d="M9 2 4 7l5 5" fill="none" stroke="#333" stroke-width="2"/></svg></span>
  <span class="hero-arrow next"><svg width="14" height="14" viewBox="0 0 14 14"><path d="M5 2l5 5-5 5" fill="none" stroke="#333" stroke-width="2"/></svg></span>
  <aside class="hero-panel">
    <h3 class="panel-title">RSVP</h3>
    <div class="field">Event ID</div>
    <div class="field-row">Attending <div class="field">Yes</div> No <div class="field">0</div></div>
    <span class="btn-orange">Submit RSVP</span>
    <div class="panel-split"></div>
    <h3 class="panel-title">Suppliers</h3>
    <div class="field">Category</div>
    <div class="field">Sub Category</div>
    <div class="field">Location</div>
    <div class="range"><span></span></div>
    <span class="btn-orange wide">Search for Suppliers</span>
  </aside>
</section>

<section class="categories">
  <div class="wrap">
    <h2 class="section-title">Categories</h2>
    <div class="cat-grid">
      <div class="cat-item">
        <div class="cat-head"><span class="cat-icon"><svg width="22" height="22" viewBox="0 0 22 22"><circle cx="11" cy="11" r="7" fill="none" stroke="#f5b31b" stroke-width="2"/></svg></span><h3>Birthdays &amp;<br>Anniversaries</h3></div>
        <p>Neque porro quisquam est qui dolorem ipsum quia dolor sit amet consectetur.</p>
      </div>
      <div class="cat-item">
        <div class="cat-head"><span class="cat-icon"><svg width="22" height="22" viewBox="0 0 22 22"><path d="M11 18 4 11a4 4 0 0 1 7-5 4 4 0 0 1 7 5z" fill="none" stroke="#f5b31b" stroke-width="2"/></svg></span><h3>Weddings</h3></div>
        <p>Ut enim ad minima veniam quis nostrum exercitationem ullam corporis suscipit.</p>
      </div>
      <div class="cat-item">
        <div class="cat-head"><span class="cat-icon"><svg width="22" height="22" viewBox="0 0 22 22"><rect x="4" y="7" width="14" height="10" fill="none" stroke="#f5b31b" stroke-width="2"/></svg></span><h3>Conferences</h3></div>
        <p>Quis autem vel eum iure reprehenderit qui in ea voluptate velit esse quam.</p>
      </div>
      <div class="cat-item">
        <div class="cat-head"><span class="cat-icon"><svg width="22" height="22" viewBox="0 0 22 22"><path d="M8 16V5l9-2v11" fill="none" stroke="#f5b31b" stroke-width="2"/></svg></span><h3>Musical Events</h3></div>
        <p>Temporibus autem quibusdam et aut officiis debitis aut rerum necessitatibus.</p>
      </div>
    </div>
  </div>
</section>

<section class="ad-band">
  <div class="wrap"><span class="ad-label">ADS</span></div>
  <div class="ad-offer">30 % Discount on Purchase</div>
</section>

<section class="gifts">
  <div class="wrap">
    <h2 class="section-title">Buy Gifts</h2>
    <div class="gift-body">
      <div class="gift-photo" role="img" aria-label="Wrapped gift box with red ribbon">
        <span class="price">$15.5</span>
      </div>
      <div class="gift-text">
        <h3>Ducimus Qui Blanditiis</h3>
        <p>Sed ut perspiciatis unde omnis iste natus error sit voluptatem accusantium doloremque laudantium, totam rem aperiam eaque ipsa quae ab illo inventore veritatis et quasi architecto beatae vitae dicta sunt explicabo.</p>
        <p>Nemo enim ipsam voluptatem quia voluptas sit aspernatur aut odit aut fugit, sed quia consequuntur magni dolores eos qui ratione voluptatem sequi nesciunt.</p>
        <div class="pager">
          <span><svg width="12" height="12" viewBox="0 0 12 12"><path d="M8 2 4 6l4 4" fill="none" stroke="#f5b31b" stroke-width="2"/></svg></span>
          <span><svg width="12" height="12" viewBox="0 0 12 12"><path d="M4 2l4 4-4 4" fill="none" stroke="#f5b31b" stroke-width="2"/></svg></span>
        </div>
      </div>
    </div>
  </div>
</section>

<section class="suppliers">
  <div class="wrap">
    <h2 class="section-title center">Suppliers</h2>
    <div class="sup-grid">
      <div class="sup-card">
        <div class="sup-photo" role="img" aria-label="Decorated party tent" style="background:linear-gradient(135deg,#c7a36b,#f0e3c8 60%,#8f6b3a)"></div>
        <div class="stars">★★★★★</div>
        <h4>Galmesa Party Supplies</h4>
        <p>142 Linden Street<br>Meadow, NY 10482<br>United States</p>
      </div>
      <div class="sup-card">
        <div class="sup-photo" role="img" aria-label="Stage with blue concert lights" style="background:linear-gradient(135deg,#2b2f78,#7b4fc2 55%,#d24b8a)"></div>
        <div class="stars">★★★★<span class="off">★</span></div>
        <h4>Vortune Sound Rigs</h4>
        <p>88 Harbor Road<br>Delta, Texas<br>TX 75012, USA</p>
      </div>
      <div class="sup-card">
        <div class="sup-photo" role="img" aria-label="Banquet hall with pink decorations" style="background:linear-gradient(135deg,#e7a9b8,#f7e2d2 55%,#c97b8a)"></div>
        <div class="stars">★★★★★</div>
        <h4>Crumbel Bakehouse</h4>
        <p>27 Orchard Lane<br>Lake Ridge, Nevada<br>United States</p>
      </div>
    </div>
  </div>
</section>

<div class="spacer"></div>

<section class="ad-band">
  <div class="wrap"><span class="ad-label">ADS</span></div>
  <div class="ad-offer tall">20 % Discount<br>On This Winter</div>
</section>

<section class="events">
  <div class="wrap">
    <h2 class="section-title center">Recent Events</h2>
    <div class="event-list">
      <article class="event">
        <div class="event-thumb" role="img" aria-label="Event photo" style="background:linear-gradient(135deg,#8a5a3c,#d8b58a)"></div>
        <div class="event-main">
          <h4>Nam libero tempore</h4>
          <p>Nam libero tempore cum soluta nobis est eligendi optio cumque nihil impedit quo minus id quod maxime placeat facere possimus omnis voluptas assumenda est.</p>
          <p>142 Linden Street, Meadow, NY, United States<br><span class="link">info@zorveno.com</span></p>
        </div>
        <div class="event-meta"><b>Share</b><span>12 Comments</span><span class="stars">★★★★<span class="off">★</span></span></div>
      </article>
      <article class="event">
        <div class="event-thumb" role="img" aria-label="Event photo" style="background:linear-gradient(135deg,#3c4a6a,#b59a7a)"></div>
        <div class="event-main">
          <h4>Sed Ut Perspiciatis</h4>
          <p>At vero eos et accusamus et iusto odio dignissimos ducimus qui blanditiis praesentium voluptatum deleniti atque corrupti quos dolores et quas molestias.</p>
          <p>88 Harbor Road, Delta, TX, United States<br><span class="link">www.zorveno.com</span></p>
        </div>
        <div class="event-meta"><b>Share</b><span>8 Comments</span><span class="stars">★★★★★</span></div>
      </article>
      <article class="event">
        <div class="event-thumb" role="img" aria-label="Event photo" style="background:linear-gradient(135deg,#6a3c4a,#e0b8a0)"></div>
        <div class="event-main">
          <h4>Nemo Enim Ipsam</h4>
          <p>Itaque earum rerum hic tenetur a sapiente delectus ut aut reiciendis voluptatibus maiores alias consequatur aut perferendis doloribus asperiores repellat.</p>
          <p>27 Orchard Lane, Lake Ridge, NV, United States<br><span class="link">info@zorveno.com</span></p>
        </div>
        <div class="event-meta"><b>Share</b><span>5 Comments</span><span class="stars">★★★<span class="off">★★</span></span></div>
      </article>
    </div>
  </div>
</section>

<section class="testimonials">
  <div class="wrap">
    <h2 class="section-title center">People Saying</h2>
    <div class="quote-box">
      <p>“Similique sunt in culpa qui officia deserunt mollitia animi id est laborum et dolorum fuga.”</p>
      <span class="more">Read More</span>
      <div class="quote-nav">
        <span><svg width="10" height="10" viewBox="0 0 10 10"><path d="M7 1 3 5l4 4" fill="none" stroke="#fff" stroke-width="2"/></svg></span>
        <span><svg width="10" height="10" viewBox="0 0 10 10"><path d="M3 1l4 4-4 4" fill="none" stroke="#fff" stroke-width="2"/></svg></span>
      </div>
    </div>
    <p class="quote-author">By, Mara Quell</p>
  </div>
</section>

<footer>
  <div class="site-footer">
    <div class="wrap foot-grid">
      <div class="foot-col">
        <h4>Contact</h4>
        <div class="contact-line"><i></i>142 Linden Street, Meadow, NY 10482</div>
        <div class="contact-line"><i></i>(555) 014 2290</div>
        <div class="contact-line"><i></i>info@zorveno.com</div>
        <div class="social"><span></span><span></span><span></span><span></span></div>
      </div>
      <div class="foot-col">
        <h4>Latest Posts</h4>
        <div class="post"><div class="post-thumb" role="img" aria-label="Post photo" style="background:#c9a27a"></div><div><p>Sed ut perspiciatis unde omnis iste natus error sit.</p><a href="#">Read More</a></div></div>
        <div class="post"><div class="post-thumb" role="img" aria-label="Post photo" style="background:#8b6f9a"></div><div><p>Nemo enim ipsam voluptatem quia voluptas sit aut.</p><a href="#">Read More</a></div></div>
        <div class="post"><div class="post-thumb" role="img" aria-label="Post photo" style="background:#d28a6a"></div><div><p>Quis autem vel eum iure reprehenderit qui in ea.</p><a href="#">Read More</a></div></div>
      </div>
      <div class="foot-col">
        <h4>Select Suppliers</h4>
        <div class="faces" role="img" aria-label="Grid of supplier profile photos">
          <span style="background:#c9a88a"></span><span style="background:#8a7a6a"></span><span style="background:#d8b8a0"></span><span style="background:#6a5a4a"></span>
          <span style="background:#b89a80"></span><span style="background:#e0c8b0"></span><span style="background:#7a6a5a"></span><span style="background:#c0a090"></span>
          <span style="background:#a08a7a"></span><span style="background:#d0b098"></span><span style="background:#90786a"></span><span style="background:#e4ccb8"></span>
        </div>
      </div>
    </div>
  </div>
  <div class="foot-bottom">
    <div class="wrap">
      <span>© Copyright 2024 ZorVeno. All Rights Reserved.</span>
      <nav class="foot-links"><a class="active" href="#">Home</a><a href="#">Blog</a><a href="#">Contact Us</a></nav>
    </div>
  </div>
</footer>

</body>
</html>
```